Melodex Icon design for single song release

Design an icon for melodex (eventually, we will need to use the same style to design the 4 side CD cover) for a new song to be released. Needs to follow certain specs: I am attaching a design that I created, but looking for the design to be spiced up a bit. I am happy with the design, font, and style.. Just want to see something a bit more creative.
Specs:
1. An Melodex ICON for my latest single that i need to get released. Here are the specs..
• Finalized design for icon for Melodex: (DLT Logo attached and JPEG dimensions below)
o Name of the song is “WHEN”
Melodex: Your cover art must be:
o 1400 x 1400 pixels
o JPG file type
o 72 - 300dpi (300dpi is the best)
o Less than 25mb
o RGB color scheme (not CMYK)

I have my music logo and the picture, so I have to have something that fits these dimensions for Melodex.

Please do not change the photo. and please keep the photo in color. The song has an edge to it, but don't want over the top.

Target Market(s)

Contemporary Christian; Christian Rock - music has an edge.

Font styles to use
Other font styles liked:
• see example design

Requirements
Must have
• Marla Penwick
• Song title "When"
• Photo
• Dimensions listed above when design if final.
• Photo attached
• Logo attached
• *Please use a color photo; please use the lettering like the example; and the font colors

```html
<!DOCTYPE html>
<html lang="en">
<head>
<meta charset="utf-8">
<title>Marla Penwick – WHEN – CD wrap</title>
<link rel="stylesheet" href="https://fonts.googleapis.com/css2?family=Archivo:wght@700;800&family=Oswald:wght@400;500&display=swap">
<style>
  :root {
    --paper: #ffffff;
    --signal-red: #ff0000;
    --night: #000000;
    --sand: #dcc2a1;
    --cream: #f4e4c4;
    --ghost-grey: rgba(140, 140, 140, 0.55);
    --ghost-pink: rgba(255, 170, 170, 0.55);
    --ghost-white: rgba(255, 255, 255, 0.35);
    --mark-border: #7a5cc4;
    --rule: rgba(255, 255, 255, 0.7);
    --trim: #b5b5b5;
  }
  * { box-sizing: border-box; margin: 0; padding: 0; }
  html, body { width: 1200px; height: 285px; overflow: hidden; background: var(--paper); }
  .wrap { position: relative; width: 1200px; height: 285px; }
  .trim-marks { position: absolute; inset: 0; }
  .panel { position: absolute; top: 14px; height: 256px; overflow: hidden; }
  .panel--back { left: 14px; width: 288px; background: var(--signal-red); }
  .panel--front { left: 302px; width: 308px; background: var(--night); }
  .panel--inner { left: 610px; width: 289px; background: var(--night); }
  .panel--tray { left: 899px; width: 288px; background: var(--sand); }

  .label-mark {
    position: absolute; width: 42px; height: 42px;
    background: var(--night); border: 1px solid var(--mark-border);
    display: flex; align-items: center; justify-content: center;
    color: var(--paper);
    font: 700 13px/1 "Archivo", sans-serif; letter-spacing: 0.5px;
  }

  .title { position: absolute; font-family: "Archivo", sans-serif; font-weight: 800; line-height: 1; white-space: nowrap; transform: translateX(-50%); }
  .title__ghost { position: absolute; left: 50%; top: 50%; transform: translate(-50%, -50%); font-size: 1.32em; letter-spacing: -2px; }
  .title__word { position: relative; letter-spacing: -1px; }

  .title--back { left: 144px; top: 108px; font-size: 34px; }
  .title--back .title__ghost { color: var(--ghost-pink); }
  .title--back .title__word { color: var(--signal-red); -webkit-text-stroke: 1.2px var(--paper); }

  .title--cover { left: 228px; top: 206px; font-size: 36px; }
  .title--cover .title__ghost { color: var(--ghost-grey); }
  .title--cover .title__word { color: #222; -webkit-text-stroke: 1.2px var(--cream); }

  .title--tray { left: 136px; top: 76px; font-size: 20px; }
  .title--tray .title__ghost { color: var(--ghost-white); }
  .title--tray .title__word { color: var(--paper); }

  .artist {
    position: absolute; left: 34px; top: 136px;
    transform: translate(-50%, -50%) rotate(-90deg);
    font: 500 35px/1 "Oswald", sans-serif; letter-spacing: 2px; white-space: nowrap;
  }
  .artist__first { color: var(--signal-red); -webkit-text-stroke: 1px #777; }
  .artist__last { color: transparent; -webkit-text-stroke: 1px #cfcfcf; }

  .portrait {
    position: absolute; left: 60px; top: 0; width: 169px; height: 256px;
    background: linear-gradient(160deg, #e9d9b0 0%, #d8b58d 35%, #caa184 60%, #3a3230 85%, #1a1a1a 100%);
  }

  .tracklist { position: absolute; left: 47px; top: 106px; width: 194px; list-style: none; }
  .tracklist li { height: 19.5px; border-bottom: 1px dotted var(--rule); }
</style>
</head>
<body>
<div class="wrap">
  <svg class="trim-marks" width="1200" height="285" aria-hidden="true">
    <g stroke="var(--trim)" stroke-width="0.6" stroke-dasharray="2 2">
      <line x1="302" y1="0" x2="302" y2="12"/><line x1="302" y1="272" x2="302" y2="285"/>
      <line x1="610" y1="0" x2="610" y2="12"/><line x1="610" y1="272" x2="610" y2="285"/>
      <line x1="899" y1="0" x2="899" y2="12"/><line x1="899" y1="272" x2="899" y2="285"/>
    </g>
    <g stroke="var(--trim)" stroke-width="0.6">
      <line x1="14" y1="0" x2="14" y2="10"/><line x1="1187" y1="0" x2="1187" y2="10"/>
      <line x1="14" y1="275" x2="14" y2="285"/><line x1="1187" y1="275" x2="1187" y2="285"/>
    </g>
  </svg>

  <section class="panel panel--back">
    <div class="label-mark" style="left:123px; top:108px;">DLT</div>
    <div class="title title--back" style="top:174px;"><span class="title__ghost">WHEN</span><span class="title__word">WHEN</span></div>
  </section>

  <section class="panel panel--front">
    <div class="artist"><span class="artist__first">MARLA</span><span class="artist__last">PENWICK</span></div>
    <div class="portrait" role="img" aria-label="Colour portrait photo of the artist, blonde hair, dark top"></div>
    <div class="label-mark" style="left:209px; top:16px;">DLT</div>
    <div class="title title--cover"><span class="title__ghost">WHEN</span><span class="title__word">WHEN</span></div>
  </section>

  <section class="panel panel--inner">
    <div class="artist"><span class="artist__first">MARLA</span><span class="artist__last">PENWICK</span></div>
    <div class="portrait" role="img" aria-label="Colour portrait photo of the artist, blonde hair, dark top"></div>
    <div class="label-mark" style="left:209px; top:16px;">DLT</div>
    <div class="title title--cover"><span class="title__ghost">WHEN</span><span class="title__word">WHEN</span></div>
  </section>

  <section class="panel panel--tray">
    <div class="label-mark" style="left:115px; top:24px;">DLT</div>
    <div class="title title--tray"><span class="title__ghost">WHEN</span><span class="title__word">WHEN</span></div>
    <ul class="tracklist" aria-hidden="true">
      <li></li><li></li><li></li><li></li><li></li><li></li>
    </ul>
  </section>
</div>
</body>
</html>
```